Copper Sprinter

I'm looking for an advertising banner for a fitness programme I'm releasing on Chatterloop. It needs to be centered around indoor rowing and appeal to both men and women. If you wanted to incorporate an indoor rowing machine, I'd prefer the Veltrax 9 over others.

Fitness

```html
<!DOCTYPE html>
<html lang="en">
<head>
<meta charset="utf-8">
<title>Copper Sprinter – Indoor Rowing – 6 Weeks Programme</title>
<link rel="stylesheet" href="https://fonts.googleapis.com/css2?family=Roboto+Condensed:wght@700&display=swap">
<style>
  :root {
    --night: #050302;
    --ember: #e0641a;
    --ember-deep: #6b2a08;
    --glow: #ffb040;
    --frame-line: #e07a1c;
    --title-grey: rgba(228, 228, 228, 0.9);
    --headline-yellow: #fff200;
    --headline-orange: #ff8c00;
    --corner-grey: #767676;
    --corner-text: #eeeeee;
  }
  * { margin: 0; padding: 0; box-sizing: border-box; }
  html, body {
    width: 1200px;
    height: 444px;
    overflow: hidden;
    background: var(--night);
  }
  .banner {
    position: relative;
    width: 1200px;
    height: 444px;
    overflow: hidden;
    background: var(--night);
    font-family: "Roboto Condensed", "Arial Narrow", sans-serif;
    font-weight: 700;
    text-transform: uppercase;
  }
  .athlete-photo {
    position: absolute;
    inset: 0;
    background:
      radial-gradient(ellipse 170px 90px at 390px 420px, rgba(255, 176, 64, 0.85), rgba(224, 100, 26, 0) 100%),
      radial-gradient(ellipse 300px 380px at 180px 150px, rgba(224, 100, 26, 0.95), rgba(107, 42, 8, 0.75) 55%, rgba(5, 3, 2, 0) 100%),
      radial-gradient(ellipse 220px 160px at 700px 40px, rgba(150, 60, 10, 0.35), rgba(5, 3, 2, 0) 100%),
      linear-gradient(90deg, var(--ember-deep) 0%, rgba(40, 14, 3, 0.9) 40%, var(--night) 65%);
  }
  .corner-band {
    position: absolute;
    left: 0;
    top: 0;
    width: 1200px;
    height: 444px;
  }
  .title-frame {
    position: absolute;
    left: 38px;
    top: 78px;
    width: 639px;
    height: 270px;
    border: 1.5px solid var(--frame-line);
  }
  .title {
    position: absolute;
    left: 82px;
    color: var(--title-grey);
    font-size: 128px;
    line-height: 1;
    white-space: nowrap;
  }
  .title--first { top: 81px; }
  .title--second { top: 205px; }
  .headline {
    position: absolute;
    left: 613px;
    font-size: 47px;
    line-height: 1;
    white-space: nowrap;
  }
  .headline--one { top: 127px; color: var(--headline-yellow); }
  .headline--two { top: 190px; color: var(--headline-yellow); }
  .headline--three { top: 247px; color: var(--headline-orange); }
  .weeks-number {
    position: absolute;
    left: 800px;
    top: 260px;
    font-size: 186px;
    line-height: 1;
    color: #ffffff;
  }
  .weeks-label {
    position: absolute;
    left: 930px;
    font-size: 45px;
    line-height: 1;
    color: var(--corner-text);
    white-space: nowrap;
  }
  .weeks-label--top { top: 315px; }
  .weeks-label--bottom { top: 366px; }
</style>
</head>
<body>
  <main class="banner">
    <div class="athlete-photo" role="img" aria-label="Athlete training on an indoor rowing machine, lit by warm orange light with glowing embers below"></div>

    <svg class="corner-band" viewBox="0 0 1200 444" aria-hidden="true">
      <polygon points="688,444 1200,137 1200,444" fill="var(--corner-grey)"/>
    </svg>

    <div class="title-frame"></div>
    <h1>
      <span class="title title--first">Copper</span>
      <span class="title title--second">Sprinter</span>
    </h1>

    <p class="headline headline--one">Indoor Rowing</p>
    <p class="headline headline--two">Interval Training</p>
    <p class="headline headline--three">Sessions</p>

    <p class="weeks-number">6</p>
    <p class="weeks-label weeks-label--top">Weeks</p>
    <p class="weeks-label weeks-label--bottom">Programme</p>
  </main>
</body>
</html>
```